One of Australia's fastest growing Financial Company looking for an updated business card design!

Meridale Partners Australia is looking for an updated design for our business cards. We would like to keep up our professional appearances and have get new exciting design that fits our company.

The Meridale aim is to facilitate and assist clients in every financial requirement that may arise in financial areas.

We would to see the design to use colour blue and we like the clouds in the background. We have attached two designs we have use before but we need something with more professional and easy to read design.

We would like the website in the back of the card; the employees name more central and stands out; only a postal address; a list of all our locations along the bottom (Sydney, Melbourne, Brisbane, Singapore)

Looking forward to seeing the designs come in!

Target Market(s)

Other Industry Professionals
Middle Class Families

Industry/Entity Type

Finance

Contact Information for Business Card

Name; Company Role; Office Number; Mobile Number; Email Address; Website; Postal Address; Locations

Font styles to use
Serif
Sans Serif

Colors
0492cd
33a6d7
85cae6
85acd3
3176b5
0455a3
cee9f5
d5e2ee

Requirements
Must have
• Name; Company Role; Office Number; Mobile Number; Email Address; Website; Postal Address; Locations
Nice to have
• The colour blue, clouds on the background

```html
<!DOCTYPE html>
<html lang="en">
<head>
<meta charset="utf-8">
<title>Meridale Partners Australia – Business Card</title>
<link href="https://fonts.googleapis.com/css2?family=Open+Sans:wght@400;600;700&display=swap" rel="stylesheet">
<style>
  :root {
    --blue-deep: #1a76c2;
    --blue-mid: #2a9bd9;
    --blue-light: #4fb3e6;
    --accent-red: #d7212f;
    --ink-grey: #5a5a5a;
    --paper: #ffffff;
    --backdrop: #2b2b2b;
  }
  * { margin: 0; padding: 0; box-sizing: border-box; }
  html, body { width: 1200px; height: 1200px; overflow: hidden; }
  body {
    background: var(--backdrop);
    font-family: "Open Sans", sans-serif;
    position: relative;
  }
  .card {
    position: absolute;
    width: 740px;
    height: 420px;
    border-radius: 38px;
    overflow: hidden;
    box-shadow: 0 10px 24px rgba(0,0,0,.45);
  }

  /* Front */
  .card-front {
    left: 130px; top: 150px;
    background: linear-gradient(160deg, var(--blue-light) 0%, var(--blue-mid) 45%, var(--blue-deep) 100%);
    color: var(--paper);
  }
  .world-map-area {
    position: absolute;
    left: 60px; top: 40px; width: 620px; height: 300px;
    border-radius: 40px;
    background: radial-gradient(ellipse at center, rgba(255,255,255,.12) 0%, rgba(255,255,255,0) 70%);
  }
  .front-brand {
    position: absolute;
    left: 0; right: 0; top: 120px;
    text-align: center;
  }
  .brand-name {
    font-weight: 700;
    font-size: 104px;
    line-height: 1;
    letter-spacing: -1px;
  }
  .front-url {
    font-size: 19px;
    font-weight: 600;
    margin-top: 6px;
  }
  .locations {
    position: absolute;
    left: 0; right: 0; bottom: 34px;
    text-align: center;
    font-weight: 700;
    font-size: 21px;
    letter-spacing: .3px;
  }
  .locations .dot {
    display: inline-block;
    width: 10px; height: 10px;
    border-radius: 50%;
    background: var(--accent-red);
    margin: 0 10px 2px;
    vertical-align: middle;
  }

  /* Back */
  .card-back {
    left: 330px; top: 630px;
    background: var(--paper);
  }
  .back-brand {
    position: absolute;
    left: 60px; top: 30px;
    color: var(--blue-mid);
    font-weight: 700;
    font-size: 78px;
    line-height: 1;
    letter-spacing: -1px;
  }
  .person {
    position: absolute;
    left: 62px; top: 120px;
  }
  .person-name {
    color: var(--blue-deep);
    font-weight: 700;
    font-size: 27px;
    line-height: 1.3;
    letter-spacing: .5px;
  }
  .person-role {
    color: var(--ink-grey);
    font-size: 16px;
    line-height: 1.4;
    letter-spacing: .4px;
  }
  .waves {
    position: absolute;
    left: 0; top: 0;
    width: 740px; height: 420px;
  }
  .contacts {
    position: absolute;
    right: 36px; top: 278px;
    text-align: right;
    color: var(--paper);
    font-size: 16px;
    line-height: 23px;
  }
  .contacts li {
    list-style: none;
    display: flex;
    justify-content: flex-end;
    align-items: center;
    gap: 10px;
  }
  .icon {
    width: 19px; height: 19px;
    border-radius: 50%;
    background: var(--accent-red);
    display: inline-flex;
    align-items: center;
    justify-content: center;
  }
  .address {
    position: absolute;
    right: 36px; bottom: 20px;
    color: var(--paper);
    font-weight: 700;
    font-size: 17px;
    line-height: 22px;
    letter-spacing: .3px;
  }
</style>
</head>
<body>

<section class="card card-front">
  <div class="world-map-area" role="img" aria-label="Faint world map in the background"></div>
  <div class="front-brand">
    <div class="brand-name">Meridale</div>
    <div class="front-url">www.meridalepartnersaustralia.com</div>
  </div>
  <div class="locations">
    SYDNEY<span class="dot"></span>MELBOURNE<span class="dot"></span>BRISBANE<span class="dot"></span>SINGAPORE
  </div>
</section>

<section class="card card-back">
  <svg class="waves" viewBox="0 0 740 420" preserveAspectRatio="none" aria-hidden="true">
    <defs>
      <linearGradient id="waveBlue" x1="0" y1="0" x2="1" y2="1">
        <stop offset="0" stop-color="#3aa9e0"/>
        <stop offset="1" stop-color="#1a76c2"/>
      </linearGradient>
    </defs>
    <path d="M0 214 C160 272 320 286 470 246 C580 216 660 206 740 214 L740 238 C660 230 580 240 470 270 C320 310 160 298 0 238 Z" fill="#d7212f"/>
    <path d="M0 248 C170 310 330 318 470 278 C580 248 660 240 740 248 L740 420 L0 420 Z" fill="url(#waveBlue)"/>
    <path d="M40 270 C150 312 250 324 330 316" fill="none" stroke="#ffffff" stroke-width="4" stroke-linecap="round"/>
  </svg>

  <div class="back-brand">Meridale</div>
  <div class="person">
    <div class="person-name">JOANNA WHITFIELD</div>
    <div class="person-role">INVESTMENT CONSULTANT<br>PREMIUM BANKING SERVICES</div>
  </div>

  <ul class="contacts">
    <li>0412 555 018 <span class="icon"><svg width="11" height="11" viewBox="0 0 24 24"><path fill="#fff" d="M6.6 10.8a15 15 0 0 0 6.6 6.6l2.2-2.2c.3-.3.7-.4 1-.2 1.1.4 2.3.6 3.6.6.6 0 1 .4 1 1V20c0 .6-.4 1-1 1A17 17 0 0 1 3 4c0-.6.4-1 1-1h3.5c.6 0 1 .4 1 1 0 1.3.2 2.5.6 3.6.1.3 0 .7-.2 1z"/></svg></span></li>
    <li>(02) 5550 1234 <span class="icon"><svg width="11" height="11" viewBox="0 0 24 24"><rect x="5" y="3" width="14" height="18" rx="2" fill="#fff"/></svg></span></li>
    <li>www.meridalepartnersaustralia.com <span class="icon"><svg width="11" height="11" viewBox="0 0 24 24"><circle cx="12" cy="12" r="9" fill="none" stroke="#fff" stroke-width="2"/><path d="M3 12h18M12 3c3 3 3 15 0 18M12 3c-3 3-3 15 0 18" fill="none" stroke="#fff" stroke-width="2"/></svg></span></li>
    <li>joanna@meridalepartnersaustralia.com <span class="icon"><svg width="11" height="11" viewBox="0 0 24 24"><rect x="3" y="6" width="18" height="12" rx="1" fill="#fff"/><path d="M3 6l9 7 9-7" fill="none" stroke="#d7212f" stroke-width="2"/></svg></span></li>
  </ul>
  <div class="address">PO BOX 4820, KELLMORE RIDGE, NSW 2199</div>
</section>

</body>
</html>
```